Brindle Advisory Business Card Design

Business card for business consulting company, using attached logo. We do financial and strategic consulting, and want a clean, professional image with a bit of fun. Our logo is a flat whale tail, which symbolizes the Orca whale, a highly collaborative, group based animal that is very successful in navigating the ocean, protecting the herd, and hunting. We like the logo that is blue and gray on white one one side, but would be open to a blue card with white lettering on the other side... or whatever you'd suggest
Updates
Hi all - I have had the logo modified to take the shadowing off the tail. I will post it on the brief... under a file name called updated logo. thank you Added Saturday, April 25, 2015
Target Market(s)
Small to medium sized businesses ($10M to $500M in revenue per year), financial and sales executives, general managers, attorneys and CPAs
Industry/Entity Type
Financial
Contact Information for Business Card
Want company name, contact info - name, title, telephone, email, website, linkedin, twitter and Facebook. No physical address yet.
Requirements
Must have
- contemporary design, bold, strong, confident but with a bit of fun. prominently feature the logo and the whale tail icon
Nice to have
- unique touches that would differentiate us from a regular card... for example, logo and writing all on front on white background, but on back - logo in white on a blue background
- open to idea of different shapes of card than standard... but not sure
Should not have
- ?

```html
<!DOCTYPE html>
<html lang="en">
<head>
<meta charset="utf-8">
<title>Brindle Advisory Business Card</title>
<link rel="stylesheet" href="https://fonts.googleapis.com/css2?family=Arimo:ital,wght@0,400;0,700;1,400&display=swap">
<style>
  :root {
    --page: #ffffff;
    --frame: #5a5a5a;
    --card-edge: #52618f;
    --brand-blue: #0a55a3;
    --brand-navy: #173a6b;
    --ink: #111111;
    --muted: #7a7a7a;
    --dots: #777777;
  }
  * { margin: 0; padding: 0; box-sizing: border-box; }
  html, body {
    width: 1200px; height: 467px; overflow: hidden;
    background: var(--page);
    font-family: "Arimo", Arial, sans-serif;
  }
  .sheet {
    position: relative; width: 1200px; height: 467px;
    border: 1px solid var(--frame);
  }
  .side-label {
    position: absolute; top: 20px; font-size: 30px; color: var(--ink);
    transform: translateX(-50%);
  }
  .side-label--front { left: 312px; }
  .side-label--back { left: 901px; }
  .card {
    position: absolute; top: 65px; height: 367px;
    border: 1px solid var(--card-edge); background: var(--page);
  }
  .card--front { left: 20px; width: 567px; }
  .card--back { left: 608px; width: 572px; }

  .brand { position: absolute; display: flex; align-items: center; }
  .brand__mark { background: var(--brand-navy); border-radius: 6px; flex: none; }
  .brand__text { position: relative; }
  .brand__name {
    color: var(--brand-navy); font-weight: 700; letter-spacing: -1px; line-height: 1;
    display: block;
  }
  .brand__tagline {
    display: block; text-align: right; color: var(--brand-navy); line-height: 1;
  }
  .card--front .brand { left: 88px; top: 127px; }
  .card--front .brand__mark { width: 68px; height: 68px; margin-right: 10px; }
  .card--front .brand__name { font-size: 41px; }
  .card--front .brand__tagline { font-size: 13px; margin-top: 3px; }
  .card--back .brand { left: 31px; top: 167px; }
  .card--back .brand__mark { width: 34px; height: 35px; margin-right: 5px; border-radius: 3px; }
  .card--back .brand__name { font-size: 21px; letter-spacing: -0.5px; }
  .card--back .brand__tagline { font-size: 7px; margin-top: 2px; }

  .web-band {
    position: absolute; left: 0; right: 0; top: 278px; height: 44px;
    background: var(--brand-blue); color: #fff; font-size: 21px;
    display: flex; align-items: center; justify-content: center;
  }

  .divider {
    position: absolute; left: 282px; top: 36px; height: 295px;
    border-left: 2px dotted var(--dots);
  }
  .contact {
    position: absolute; right: 24px; text-align: right; color: var(--brand-blue);
  }
  .contact__name { top: 34px; font-size: 26px; }
  .contact__title { top: 70px; font-size: 18px; font-style: italic; }
  .contact__phone { top: 127px; font-size: 18px; }
  .contact__email { top: 153px; font-size: 18px; }
  .socials { position: absolute; right: 28px; top: 195px; list-style: none; }
  .socials__item {
    display: flex; align-items: center; justify-content: flex-end;
    height: 40px; margin-bottom: 9px; color: var(--brand-blue); font-size: 18px;
  }
  .socials__dot {
    width: 40px; height: 40px; border-radius: 50%; background: var(--brand-blue);
    margin-left: 6px;
  }
</style>
</head>
<body>
<div class="sheet">
  <div class="side-label side-label--front">Front</div>
  <div class="side-label side-label--back">Back</div>

  <section class="card card--front" aria-label="Card front">
    <div class="brand">
      <span class="brand__mark"></span>
      <span class="brand__text">
        <span class="brand__name">brindleadvisory</span>
        <span class="brand__tagline">business consulting</span>
      </span>
    </div>
    <div class="web-band">www.brindleadvisory.com</div>
  </section>

  <section class="card card--back" aria-label="Card back">
    <div class="brand">
      <span class="brand__mark"></span>
      <span class="brand__text">
        <span class="brand__name">brindleadvisory</span>
        <span class="brand__tagline">business consulting</span>
      </span>
    </div>
    <div class="divider"></div>
    <div class="contact contact__name">Daniel Hart</div>
    <div class="contact contact__title">CEO</div>
    <div class="contact contact__phone">+91 02224550187</div>
    <div class="contact contact__email">daniel@brindleadvisory.in</div>
    <ul class="socials">
      <li class="socials__item">brindleadv<span class="socials__dot"></span></li>
      <li class="socials__item">brindleadv<span class="socials__dot"></span></li>
      <li class="socials__item">brindleadv<span class="socials__dot"></span></li>
    </ul>
  </section>
</div>
</body>
</html>
```